Luxury Candle Startup Needs Modern Packaging Box & Matching Label Design

We are Lunavale, a luxury candle company about to launch in Australia and we need a box packaging design that is modern, minimalist, and feminine. Our target audience are females, mostly mothers, within the age range of 25-45 who are looking for high quality, handmade luxurious products. Our company is going to have a large social media presence with new mothers as we are going to show our journey with starting a business whilst on maternity leave. We would like the arch shape incorporated into the box packaging as it is beautiful and symbolises moving into a new phase in life which really represents the brand. We would like for the packaging box to be a simple white box with a sleeve insert over the box with the design to make printing easier. Our colour inspiration are very earthy colours and would like the sleeve colour to be easily changed according to the scent. For example dusky rose coloured sleeve for rose patchouli and amber scent, light coffee coloured sleeve for coffee bean cacao scent etc. Please see uploaded files for inspiration, our logo, and the type of candle jars used.
The box dimensions are:
External Dimension: 95mmW x 95mmL x 116mmH
We look forward to seeing your amazing designs!

```html
<!DOCTYPE html>
<html lang="en">
<head>
<meta charset="UTF-8">
<title>Lunavale – Coffee Bean · Cacao Box Sleeve</title>
<link rel="stylesheet" href="https://fonts.googleapis.com/css2?family=Oswald:wght@400;500;600&family=Josefin+Sans:wght@400&family=Allura&display=swap">
<style>
  :root {
    --canvas-bg: #f4f4f4;
    --box-white: #ffffff;
    --box-edge: #e4e4e4;
    --sleeve-coffee: #dec2a8;
    --arch-line: #ffffff;
    --ink: #2e2a27;
  }
  html, body {
    margin: 0;
    padding: 0;
    width: 1200px;
    height: 1200px;
    overflow: hidden;
    background: var(--canvas-bg);
  }
  .canvas {
    position: relative;
    width: 1200px;
    height: 1200px;
  }
  .box-front {
    position: absolute;
    left: 220px;
    top: 136px;
    width: 760px;
    height: 928px;
    background: var(--box-white);
    box-shadow: 0 0 0 1px var(--box-edge);
  }
  .sleeve {
    position: absolute;
    left: 120px;
    top: 0;
    width: 520px;
    height: 928px;
    background: var(--sleeve-coffee);
  }
  .sleeve-art {
    display: block;
    width: 520px;
    height: 928px;
  }
  .arch-frame {
    fill: none;
    stroke: var(--arch-line);
    stroke-width: 3;
  }
  .arch-tagline {
    font-family: "Oswald", sans-serif;
    font-weight: 600;
    font-size: 17px;
    fill: var(--ink);
  }
  .brand-name {
    font-family: "Oswald", sans-serif;
    font-weight: 400;
    font-size: 44px;
    letter-spacing: 3px;
    fill: var(--ink);
  }
  .brand-sub {
    font-family: "Josefin Sans", sans-serif;
    font-size: 10.5px;
    letter-spacing: 1.5px;
    fill: var(--ink);
  }
  .brand-sub--small {
    font-size: 8.5px;
  }
  .scent-name {
    font-family: "Allura", cursive;
    font-size: 62px;
    fill: var(--ink);
  }
  .scent-rule {
    stroke: var(--arch-line);
    stroke-width: 1.5;
  }
  .origin-line,
  .size-line {
    font-family: "Oswald", sans-serif;
    font-weight: 500;
    font-size: 17px;
    letter-spacing: 3px;
    fill: var(--ink);
  }
</style>
</head>
<body>
<main class="canvas">
  <section class="box-front">
    <div class="sleeve">
      <svg class="sleeve-art" viewBox="0 0 520 928" xmlns="http://www.w3.org/2000/svg">
        <defs>
          <path id="tagline-arc" d="M 58 372 A 204 204 0 1 1 462 372"/>
        </defs>
        <path class="arch-frame" d="M 23 872 L 23 342 A 237 237 0 0 1 497 342 L 497 872 Z"/>
        <text class="arch-tagline" text-anchor="middle">
          <textPath href="#tagline-arc" startOffset="50%" textLength="610" lengthAdjust="spacing">HANDMADE HIGH QUALITY LUXURY CANDLE</textPath>
        </text>
        <text class="brand-name" x="260" y="393" text-anchor="middle">LUNAVALE</text>
        <text class="brand-sub" x="260" y="427" text-anchor="middle">LUXURY FRAGRANCE</text>
        <text class="brand-sub brand-sub--small" x="260" y="444" text-anchor="middle">AUSTRALIA</text>
        <text class="scent-name" x="260" y="612" text-anchor="middle">Coffee bean · Cacao</text>
        <line class="scent-rule" x1="80" y1="636" x2="444" y2="632"/>
        <text class="origin-line" x="260" y="684" text-anchor="middle">MADE IN AUSTRALIA</text>
        <text class="size-line" x="260" y="833" text-anchor="middle">4 OZ · 120 H</text>
      </svg>
    </div>
  </section>
</main>
</body>
</html>
```